Educational Construction Organization needs Flyer for Upcoming Forum

We need a SAVE THE DATE Flyer for our 2020 Ravteq Forum. We work with Architects, Engineers, Contractors and Owners in the design and construction industry. Our mission is to evolve the capital projects industry through sharing of knowledge for optimized leadership, delivery and performance. The final design should communicate the connection between these industry professionals, our mission, and the Forum theme and byline.
Updates

Need extra days to review

Target Market(s)

Design and construction industry.

Industry/Entity Type

Construction

Font styles to use
Sans Serif

Colors

Designer to choose colors to be used in the design.

Requirements
Must have
• Title, By-line, 3 key topics, Date and location. Design that implements the theme with graphic(s) (not just text).
• NEW TITLE: FUTURE PROOFING: Connecting the dots to make sense of the "SMART" City
• 3 Key Topics: Smart Cities, Smart Institutions, Smart Connections
• Date: April 1-3, 2020
• Location: San Antonio, TX
Nice to have
• Please review attached problem statement for a better understanding of what this Forum will focus on when designing your graphic for the flyer.

```html
<!DOCTYPE html>
<html lang="en">
<head>
<meta charset="utf-8">
<title>Ravteq Forum 2020 – Save the Date</title>
<link href="https://fonts.googleapis.com/css2?family=Oswald:wght@300;400;500;600;700&display=swap" rel="stylesheet">
<style>
  :root {
    --stage: #5a5a5a;
    --brand-blue: #2f4a9e;
    --deep-blue: #2a4596;
    --brand-green: #8cc63f;
    --paper: #ffffff;
    --mist: #e4e4e6;
    --ink: #333333;
    --logo-grey: #555555;
    --headline-light: #efefef;
  }
  html, body {
    margin: 0;
    width: 1200px;
    height: 1200px;
    overflow: hidden;
    background: var(--stage);
  }
  .canvas { display: block; width: 1200px; height: 1200px; }
  .display { font-family: 'Oswald', sans-serif; }
  .headline-main { font-weight: 700; fill: var(--headline-light); }
  .headline-sub { font-weight: 600; fill: var(--paper); }
  .headline-accent { font-weight: 600; fill: var(--brand-green); }
  .byline-lead { font-weight: 300; fill: var(--ink); }
  .byline-theme { font-weight: 600; fill: var(--brand-blue); }
  .topic-label { font-weight: 300; fill: var(--ink); }
  .contact-phone { font-weight: 600; fill: var(--brand-green); }
  .contact-city { font-weight: 400; fill: var(--paper); font-style: italic; }
  .date-text { font-weight: 700; fill: #1d1d1d; font-style: italic; }
  .brand-name { font-weight: 500; fill: var(--logo-grey); }
  .icon-line { fill: none; stroke: var(--paper); stroke-width: 5; stroke-linecap: round; stroke-linejoin: round; }
  .icon-fill { fill: var(--paper); }
</style>
</head>
<body>
<svg class="canvas" viewBox="0 0 1932 1932" xmlns="http://www.w3.org/2000/svg">
  <defs>
    <clipPath id="flyer-clip"><rect x="290" y="92" width="1352" height="1748"/></clipPath>
    <linearGradient id="paper-fade" x1="0" y1="0" x2="0" y2="1">
      <stop offset="0" stop-color="var(--paper)"/>
      <stop offset="0.5" stop-color="#f4f4f5"/>
      <stop offset="1" stop-color="var(--mist)"/>
    </linearGradient>
    <linearGradient id="panel-blue" x1="0" y1="0" x2="0" y2="1">
      <stop offset="0" stop-color="#2a4596"/>
      <stop offset="1" stop-color="#3a56a6"/>
    </linearGradient>
    <radialGradient id="city-night" cx="0.5" cy="0.3" r="0.75">
      <stop offset="0" stop-color="#5cc4f0"/>
      <stop offset="0.45" stop-color="#1f6fc4"/>
      <stop offset="1" stop-color="#0d2f78"/>
    </radialGradient>
    <radialGradient id="burst-green" cx="0.5" cy="0.5" r="0.5">
      <stop offset="0" stop-color="#b8dd6a"/>
      <stop offset="1" stop-color="#7fb836"/>
    </radialGradient>
  </defs>

  <g class="flyer" clip-path="url(#flyer-clip)">
    <rect class="flyer-paper" x="290" y="92" width="1352" height="1748" fill="url(#paper-fade)"/>

    <!-- left panel with green sweep -->
    <path class="panel-sweep" fill="var(--brand-green)"
      d="M290,92 H780 C760,250 810,360 910,380 L900,880 C640,960 400,1150 290,1520 Z"/>
    <path class="panel-blue" fill="url(#panel-blue)"
      d="M290,92 H730 C720,250 770,350 880,520 L870,880 C620,940 400,1130 290,1490 Z"/>

    <!-- top-right arcs -->
    <path class="arc-blue" fill="var(--deep-blue)" d="M1495,380 C1560,350 1610,315 1642,288 V400 C1610,425 1560,445 1520,445 Z"/>
    <path class="arc-green" fill="var(--brand-green)" d="M1555,465 C1590,455 1620,440 1642,428 V492 C1625,505 1600,515 1580,522 Z"/>

    <!-- bottom-right green corner -->
    <path class="corner-green" fill="var(--brand-green)" d="M1390,1840 C1500,1780 1590,1700 1642,1605 V1840 Z"/>

    <!-- brand lockup -->
    <circle class="brand-dot" cx="995" cy="205" r="78" fill="var(--brand-blue)"/>
    <text class="display brand-name" x="1105" y="245" font-size="112" textLength="425" lengthAdjust="spacingAndGlyphs">Ravteq</text>

    <!-- hero image area -->
    <circle class="hero-ring" cx="1230" cy="642" r="342" fill="var(--brand-green)"/>
    <circle class="hero-image" cx="1230" cy="642" r="324" fill="url(#city-night)" role="img" aria-label="Night skyline of a smart city with glowing network connections and a wireless signal"/>

    <!-- headline -->
    <text class="display headline-main" x="312" y="612" font-size="172" textLength="490" lengthAdjust="spacingAndGlyphs">MAKING</text>
    <text class="display headline-sub" x="312" y="712" font-size="102" textLength="503" lengthAdjust="spacingAndGlyphs">SENSE OF THE</text>
    <text class="display headline-accent" x="312" y="826" font-size="118" textLength="485" lengthAdjust="spacingAndGlyphs">SMART CITY</text>

    <!-- byline -->
    <text class="display byline-lead" x="997" y="1137" font-size="62" text-anchor="middle" textLength="476" lengthAdjust="spacingAndGlyphs">Connecting the Dots for</text>
    <text class="display byline-theme" x="997" y="1210" font-size="52" text-anchor="middle" textLength="866" lengthAdjust="spacingAndGlyphs">DYNAMIC PLANNING, DESIGN AND DELIVERY</text>

    <!-- key topics -->
    <g class="topic topic-cities">
      <circle cx="608" cy="1400" r="89" fill="var(--brand-green)"/>
      <circle cx="608" cy="1400" r="78" fill="var(--brand-blue)"/>
      <rect class="icon-line" x="570" y="1368" width="34" height="70"/>
      <rect class="icon-line" x="604" y="1390" width="48" height="48"/>
      <line class="icon-line" x1="558" y1="1440" x2="658" y2="1440"/>
      <circle class="icon-fill" cx="600" cy="1360" r="12"/>
      <path class="icon-line" d="M638,1370 a14,14 0 0 1 18,0 M642,1377 a7,7 0 0 1 10,0"/>
    </g>
    <text class="display topic-label" x="607" y="1556" font-size="50" text-anchor="middle" textLength="205" lengthAdjust="spacingAndGlyphs">Smart Cities</text>

    <g class="topic topic-institutions">
      <circle cx="967" cy="1400" r="89" fill="var(--brand-green)"/>
      <circle cx="967" cy="1400" r="78" fill="var(--brand-blue)"/>
      <path class="icon-line" d="M932,1390 L967,1372 L1002,1390 Z"/>
      <path class="icon-line" d="M945,1396 V1428 M959,1396 V1428 M975,1396 V1428 M989,1396 V1428"/>
      <rect class="icon-line" x="936" y="1430" width="62" height="10"/>
      <path class="icon-line" d="M957,1356 a14,14 0 0 1 20,0 M962,1362 a7,7 0 0 1 10,0"/>
    </g>
    <text class="display topic-label" x="966" y="1556" font-size="50" text-anchor="middle" textLength="296" lengthAdjust="spacingAndGlyphs">Smart Institutions</text>

    <g class="topic topic-connections">
      <circle cx="1340" cy="1400" r="89" fill="var(--brand-green)"/>
      <circle cx="1340" cy="1400" r="78" fill="var(--brand-blue)"/>
      <path class="icon-line" d="M1298,1398 L1340,1362 L1382,1398 M1306,1392 V1432 H1374 V1392"/>
      <path class="icon-line" d="M1328,1428 V1405 L1318,1395 M1340,1428 V1390 M1352,1428 V1405 L1362,1395"/>
      <circle class="icon-fill" cx="1318" cy="1393" r="5"/>
      <circle class="icon-fill" cx="1340" cy="1387" r="5"/>
      <circle class="icon-fill" cx="1362" cy="1393" r="5"/>
    </g>
    <text class="display topic-label" x="1339" y="1556" font-size="50" text-anchor="middle" textLength="313" lengthAdjust="spacingAndGlyphs">Smart Connections</text>

    <!-- contact band -->
    <rect class="contact-band" x="290" y="1630" width="730" height="162" fill="var(--brand-blue)"/>
    <text class="display contact-phone" x="328" y="1701" font-size="54" textLength="594" lengthAdjust="spacingAndGlyphs">CALL US: (800) 555-0142</text>
    <text class="display contact-city" x="330" y="1760" font-size="46" textLength="268" lengthAdjust="spacingAndGlyphs">San Antonio, TX</text>

    <!-- date burst -->
    <polygon class="date-burst" fill="url(#burst-green)"
      points="1085,1597 1102,1630 1130,1605 1135,1642 1170,1628 1160,1663 1197,1660 1175,1690 1208,1703 1178,1722 1205,1745 1170,1752 1185,1785 1150,1780 1150,1817 1120,1798 1105,1830 1085,1800 1065,1830 1050,1798 1020,1817 1020,1780 985,1785 1000,1752 965,1745 992,1722 962,1703 995,1690 973,1660 1010,1663 1000,1628 1035,1642 1040,1605 1068,1630"/>
    <text class="display date-text" x="1085" y="1705" font-size="44" text-anchor="middle">April 1-3</text>
    <text class="display date-text" x="1085" y="1755" font-size="46" text-anchor="middle">2020</text>
  </g>
</svg>
</body>
</html>
```